TRU PEAK POWER.

I'd like my business logo.
contact name: Desmond Halvik
phone:0438275160
email: info@trupeakpower.net.au
website: www.trupeakpower.net.au

services:
solar
battery storage
LED lighting
energy saving solutions
general electrical
I'd like the design to look professional

Target Market(s)

Everyone

Industry/Entity Type

Business

Contact Information for Business Card

as described above

Requirements
Must have
• Id like the colours and the design to work well with my logo.

```html
<!DOCTYPE html>
<html lang="en">
<head>
<meta charset="utf-8">
<title>Tru Peak Power – Business Card</title>
<link href="https://fonts.googleapis.com/css2?family=Open+Sans:wght@400;700&display=swap" rel="stylesheet">
<style>
  :root {
    --backdrop: #ece9e4;
    --card: #ffffff;
    --green: #5aab3c;
    --green-light: #9ccb3b;
    --orange: #f39a1f;
    --orange-deep: #f0821e;
    --yellow: #fcc512;
    --ink: #2b2b2b;
  }
  * { margin: 0; padding: 0; box-sizing: border-box; }
  html, body {
    width: 1200px; height: 1000px; overflow: hidden;
    background: var(--backdrop);
    font-family: "Open Sans", Arial, sans-serif;
    color: var(--ink);
  }
  .business-card {
    position: absolute;
    left: 265px;
    width: 665px; height: 397px;
    background: var(--card);
    border-radius: 22px;
    overflow: hidden;
    box-shadow: 0 6px 18px rgba(0,0,0,.18);
  }
  .business-card--upper { top: 73px; }
  .business-card--lower { top: 532px; }

  .brand-name {
    position: absolute; left: 34px; top: 62px;
    display: flex; align-items: center; gap: 14px;
    font-size: 34px; font-weight: 700; letter-spacing: .5px;
    color: var(--green);
  }
  .brand-name__dot {
    width: 30px; height: 30px; border-radius: 50%;
    background: var(--orange);
  }

  .contact-person { position: absolute; left: 33px; top: 204px; }
  .contact-person__name { font-size: 24px; font-weight: 700; color: var(--green); line-height: 1.2; }
  .contact-person__role { font-size: 16px; line-height: 1.3; }

  .contact-list { position: absolute; left: 32px; top: 279px; list-style: none; }
  .contact-list li {
    display: flex; align-items: center; gap: 6px;
    font-size: 16.5px; height: 25px;
  }
  .contact-list svg { width: 15px; height: 15px; flex: none; }

  .services { position: absolute; left: 413px; top: 186px; }
  .services__title { font-size: 18px; font-weight: 700; color: var(--green); line-height: 1.35; }
  .services__list { list-style: none; }
  .services__list li {
    display: flex; align-items: center; gap: 7px;
    font-size: 16.5px; height: 25px;
  }
  .services__list svg { width: 15px; height: 15px; flex: none; }

  .accent-stripe { position: absolute; left: 0; bottom: 0; width: 665px; height: 40px; }
</style>
</head>
<body>

<svg width="0" height="0" style="position:absolute" aria-hidden="true">
  <defs>
    <linearGradient id="stripe-green" x1="0" x2="1" y1="0" y2="0">
      <stop offset="0" stop-color="#5aab3c"/><stop offset="1" stop-color="#a0cd3a"/>
    </linearGradient>
    <linearGradient id="stripe-orange" x1="0" x2="1" y1="0" y2="0">
      <stop offset="0" stop-color="#fcc512"/><stop offset="1" stop-color="#f0821e"/>
    </linearGradient>
    <symbol id="icon-tick" viewBox="0 0 16 16">
      <path d="M2 8.5 6 12.5 14 3.5" fill="none" stroke="#f39a1f" stroke-width="2.4" stroke-linecap="round" stroke-linejoin="round"/>
    </symbol>
    <symbol id="icon-phone" viewBox="0 0 16 16">
      <path d="M2 6c0-2 3-3 6-3s6 1 6 3v1h-3V5.5H5V7H2z M4 8h8l1.5 5h-11z" fill="#f39a1f"/>
    </symbol>
    <symbol id="icon-mail" viewBox="0 0 16 16">
      <rect x="1.5" y="3.5" width="13" height="9" fill="#f39a1f"/>
      <path d="M1.5 3.5 8 9l6.5-5.5" fill="none" stroke="#fff" stroke-width="1.2"/>
    </symbol>
    <symbol id="icon-web" viewBox="0 0 16 16">
      <circle cx="8" cy="8" r="6.5" fill="#f39a1f"/>
      <path d="M8 1.5v13M1.5 8h13M8 1.5c-3 3-3 10 0 13M8 1.5c3 3 3 10 0 13" fill="none" stroke="#fff" stroke-width="1"/>
    </symbol>
  </defs>
</svg>

<article class="business-card business-card--upper">
  <div class="brand-name"><span class="brand-name__dot"></span>TRU PEAK POWER</div>
  <div class="contact-person">
    <p class="contact-person__name">Desmond Halvik</p>
    <p class="contact-person__role">President</p>
  </div>
  <ul class="contact-list">
    <li><svg><use href="#icon-phone"/></svg>0438275160</li>
    <li><svg><use href="#icon-mail"/></svg>info@trupeakpower.net.au</li>
    <li><svg><use href="#icon-web"/></svg>www.trupeakpower.net.au</li>
  </ul>
  <section class="services">
    <h2 class="services__title">SERVICES</h2>
    <ul class="services__list">
      <li><svg><use href="#icon-tick"/></svg>Solar</li>
      <li><svg><use href="#icon-tick"/></svg>Battery storage</li>
      <li><svg><use href="#icon-tick"/></svg>LED lighting</li>
      <li><svg><use href="#icon-tick"/></svg>Energy saving solutions</li>
      <li><svg><use href="#icon-tick"/></svg>General electrical</li>
    </ul>
  </section>
  <svg class="accent-stripe" viewBox="0 0 665 40" aria-hidden="true">
    <polygon points="0,20 352,20 326,40 0,40" fill="url(#stripe-green)"/>
    <polygon points="340,40 384,8 665,8 665,40" fill="url(#stripe-orange)"/>
  </svg>
</article>

<article class="business-card business-card--lower">
  <div class="brand-name"><span class="brand-name__dot"></span>TRU PEAK POWER</div>
  <div class="contact-person">
    <p class="contact-person__name">Desmond Halvik</p>
    <p class="contact-person__role">President</p>
  </div>
  <ul class="contact-list">
    <li><svg><use href="#icon-phone"/></svg>0438275160</li>
    <li><svg><use href="#icon-mail"/></svg>info@trupeakpower.net.au</li>
    <li><svg><use href="#icon-web"/></svg>www.trupeakpower.net.au</li>
  </ul>
  <section class="services">
    <h2 class="services__title">SERVICES</h2>
    <ul class="services__list">
      <li><svg><use href="#icon-tick"/></svg>Solar</li>
      <li><svg><use href="#icon-tick"/></svg>Battery storage</li>
      <li><svg><use href="#icon-tick"/></svg>LED lighting</li>
      <li><svg><use href="#icon-tick"/></svg>Energy saving solutions</li>
      <li><svg><use href="#icon-tick"/></svg>General electrical</li>
    </ul>
  </section>
  <svg class="accent-stripe" viewBox="0 0 665 40" aria-hidden="true">
    <polygon points="0,20 352,20 326,40 0,40" fill="url(#stripe-green)"/>
    <polygon points="340,40 384,8 665,8 665,40" fill="url(#stripe-orange)"/>
  </svg>
</article>

</body>
</html>
```